A billboard for Harlow Ridge Construction size 36.5’ x 14.5’

Hi guys. We are purchasing a billboard and are looking for a design (size 36.5’ x 14.5’). Our slogan is "Quality you deserve, service you can count on". The goal of this billboard is brand recognition primarily letting people know we do roofs. Attached are logos that can be used if needed. Not necessarily all of them need to be used.

Target Market(s)

Residents in the local areas needing or thinking about a roof replacement

Industry/Entity Type

Roofing

Requirements
Must have
• Logo and services (roof replacement, gutters, siding, and snow removal)
Nice to have
• take a look at our website for ideas www.harlowridgeconstruction.example

```html
<!DOCTYPE html>
<html lang="en">
<head>
<meta charset="utf-8">
<title>Harlow Ridge Construction Billboard</title>
<link href="https://fonts.googleapis.com/css2?family=Bebas+Neue&display=swap" rel="stylesheet">
<style>
  :root {
    --black: #000000;
    --red: #f50000;
    --white: #ffffff;
    --stage: #e9eaec;
    --roof-dark: #5f6670;
    --roof: #767d87;
    --siding: #d3d5d9;
    --porch: #c2a46f;
  }
  * { margin: 0; padding: 0; box-sizing: border-box; }
  html, body {
    width: 1200px; height: 1129px; overflow: hidden;
    background: var(--stage);
  }
  .billboard {
    position: absolute; left: 0; top: 326px;
    width: 1200px; height: 477px;
    background: var(--black);
    font-family: "Bebas Neue", "Arial Narrow", sans-serif;
    font-weight: 400;
    overflow: hidden;
  }
  .billboard-shapes { position: absolute; inset: 0; }
  .headline {
    position: absolute; left: 40px; top: 34px;
    color: var(--red); line-height: 0.88; font-weight: 400;
  }
  .headline-top { display: block; font-size: 108px; letter-spacing: 0.5px; }
  .headline-main { display: block; font-size: 150px; letter-spacing: 1px; }
  .subline {
    position: absolute; left: 40px; top: 260px;
    color: var(--white); font-size: 52px; line-height: 1;
  }
  .brand-name {
    position: absolute; left: 60px; top: 370px; width: 340px;
    color: var(--white); font-size: 40px; line-height: 1; text-align: center;
    letter-spacing: 1px;
  }
  .web-address {
    position: absolute; right: 26px; top: 392px;
    font-size: 58px; line-height: 1; color: var(--black);
    letter-spacing: -0.5px; white-space: nowrap;
  }
  .web-address .accent { color: var(--white); }
</style>
</head>
<body>
  <section class="billboard">
    <svg class="billboard-shapes" width="1200" height="477" viewBox="0 0 1200 477">
      <defs>
        <linearGradient id="house-photo-tone" x1="0" y1="0" x2="0" y2="1">
          <stop offset="0" stop-color="var(--roof-dark)"/>
          <stop offset="0.45" stop-color="var(--roof)"/>
          <stop offset="0.68" stop-color="var(--siding)"/>
          <stop offset="0.86" stop-color="#d8d3c8"/>
          <stop offset="1" stop-color="var(--porch)"/>
        </linearGradient>
      </defs>
      <polygon class="accent-chevron" points="501,0 1200,0 1200,477 441,477 607,183" fill="var(--red)"/>
      <polygon class="house-photo" role="img" aria-label="Photo of a white two-storey house with a new grey shingle roof, three dormers and a columned front porch"
        points="528,0 1200,0 1200,374 523,374 631,183" fill="url(#house-photo-tone)"/>
    </svg>

    <h1 class="headline">
      <span class="headline-top">Quality You</span>
      <span class="headline-main">Deserve</span>
    </h1>
    <p class="subline">Service You Can Count On</p>
    <p class="brand-name">Harlow Ridge<br>Construction</p>
    <p class="web-address">HarlowRidge<span class="accent">Construction</span>.example</p>
  </section>
</body>
</html>
```